Renewal of the Ferravolt SA Website

Ferravolt SA is a metal construction company active in industrial piping, boilermaking and metal framing. We would like to renew our site.

This website must be ready to work with Wordpress.

The site will contain the following pages: Home, skills, presentation, contact.

The site must reflect the field of the metal construction sector. It must be clear and easily understandable. The objective is not to win mandates with but to present the company and its capabilities.

I have inserted the pages of our old presentations, to describe our sector but we do not want to reuse these elements, we are waiting for your creativity to surprise us. In the 2nd phase we will complete with new images if necessary and texts

Target Market(s)

International companies in the food, chemical and pharmaceutical sectors

Industry/Entity Type

Alimentaire, pharma, chimie

Number of Pages Required

4 page

Font styles to use
Sans Serif

Colors
0054AA
0677BA
7BADD7
CADEEF
E8F1F8

Requirements
Must have
• It must contain at least the requested pages, images of illustrations, places for descriptions
Should not have
• Elements that appear or disappear, too flash,

```html
<!DOCTYPE html>
<html lang="fr">
<head>
<meta charset="utf-8">
<title>Ferravolt SA</title>
<link href="https://fonts.googleapis.com/css2?family=Oswald:wght@400;500&family=Poppins:wght@400;500;600&display=swap" rel="stylesheet">
<style>
:root{
  --blue:#0054AA;
  --blue-deep:#1c45a0;
  --blue-mid:#0677BA;
  --blue-light:#7BADD7;
  --blue-pale:#CADEEF;
  --blue-faint:#E8F1F8;
  --ink:#1d1d1d;
  --grey-bg:#f2f2f2;
  --footer:#333333;
  --white:#ffffff;
}
*{margin:0;padding:0;box-sizing:border-box}
html,body{width:1200px;height:3090px;overflow:hidden}
body{font-family:'Poppins',sans-serif;color:var(--ink);background:var(--white);position:relative}
.head-font{font-family:'Oswald',sans-serif;font-weight:500;text-transform:uppercase;letter-spacing:-.3px}
section,header,footer{position:absolute;left:0;width:1200px}

/* header */
.site-header{top:0;height:90px;background:var(--white)}
.site-header .band-top{position:absolute;left:610px;top:0;width:590px;height:16px;background:var(--blue-deep)}
.site-header .band-bottom-right{position:absolute;left:610px;top:74px;width:590px;height:16px;background:var(--blue-deep)}
.brand{position:absolute;left:141px;top:22px;display:flex;align-items:center;gap:10px;font-family:'Poppins',sans-serif;font-weight:600;font-size:30px;color:var(--blue-deep)}
.brand .mark{width:26px;height:26px;border-radius:50%;background:var(--blue-deep)}
.nav{position:absolute;right:141px;top:38px;display:flex;gap:34px;font-size:12px}
.nav a{color:var(--ink);text-decoration:none}
.nav a.active{border-bottom:1px solid var(--blue-deep);padding-bottom:3px}

/* hero */
.hero{top:90px;height:528px;background:linear-gradient(180deg,#1f4e86 0%,#2a5c92 40%,#3a5a7a 70%,#2a3d55 100%)}
.hero-text{position:absolute;left:200px;top:196px;width:800px;text-align:center;color:var(--white);font-size:15px;font-weight:500;line-height:24px}
.btn{display:inline-block;font-size:13px;text-decoration:none}
.hero .btn{position:absolute;left:544px;top:300px;width:112px;height:32px;line-height:32px;text-align:center;background:var(--blue-deep);color:var(--white);font-size:11px;font-weight:600}

/* features */
.features{top:618px;height:193px;background:var(--grey-bg)}
.feature{position:absolute;top:36px;width:280px}
.feature svg{position:absolute;left:0;top:8px}
.feature h3{position:absolute;left:85px;top:0;font-size:18px;line-height:21px;font-weight:400}
.feature p{position:absolute;left:85px;top:56px;width:200px;font-size:13px;line-height:20px;color:#333}

/* about */
.about{top:811px;height:557px}
.about .photo{position:absolute;left:108px;top:65px;width:416px;height:416px;border-radius:50%;border:3px solid var(--blue-deep);background:radial-gradient(circle at 50% 40%,#c9ccd1,#8d939b 70%,#5f656d)}
.about .copy{position:absolute;left:568px;top:74px;width:490px}
.about .kicker{font-size:17px;font-weight:400}
.about h2{font-size:30px;color:var(--blue-deep);font-weight:400;line-height:36px}
.about h4{font-size:22px;color:var(--blue-deep);font-weight:400;margin-top:14px;line-height:28px}
.about p{font-size:13px;line-height:22px;margin-top:14px;letter-spacing:.2px}
.about h4+p{margin-top:6px}
.about .btn{margin-top:20px;margin-left:-3px;background:var(--blue-deep);color:var(--white);padding:10px 17px;font-size:13px}

/* skills */
.skills{top:1368px;height:540px;background:linear-gradient(180deg,#2449a0,#1f46a3 60%,#2a52b0)}
.skills h2{position:absolute;top:62px;width:100%;text-align:center;color:var(--white);font-size:32px;font-weight:400}
.skill{position:absolute;top:130px;width:291px;height:254px;background:var(--white)}
.skill .pic{height:183px}
.skill .label{height:71px;line-height:71px;text-align:center;font-size:18px;font-weight:400;position:relative}
.skill .corner{position:absolute;right:22px;bottom:0}
.skills .btn{position:absolute;left:529px;top:422px;width:142px;height:38px;line-height:38px;text-align:center;background:var(--white);color:var(--blue-deep);font-size:13px}

/* clients */
.clients{top:1908px;height:385px}
.clients h2{position:absolute;top:60px;width:100%;text-align:center;color:var(--blue-deep);font-size:32px;font-weight:400}
.clients .lead{position:absolute;top:128px;width:100%;text-align:center;font-size:18px;font-weight:500}
.logo-box{position:absolute;top:184px;width:172px;height:115px;background:var(--white);box-shadow:0 2px 10px rgba(0,0,0,.12);display:flex;align-items:center;justify-content:center;gap:8px;font-size:27px;font-weight:500;color:#333}
.logo-box .dot{width:22px;height:22px;border-radius:50%;background:var(--blue-mid)}
.round-arrow{position:absolute;top:220px}

/* testimonials */
.reviews{top:2293px;height:495px;background:var(--grey-bg)}
.reviews h2{position:absolute;top:64px;width:100%;text-align:center;color:var(--blue-deep);font-size:32px;font-weight:400}
.review-card{position:absolute;left:187px;top:160px;width:826px;height:253px;background:var(--white);box-shadow:0 2px 12px rgba(0,0,0,.08)}
.review-card p{position:absolute;left:63px;top:54px;width:700px;text-align:center;font-size:12.5px;line-height:27px;color:#333}
.review-card .author{position:absolute;top:192px;width:100%;text-align:center;color:var(--blue-deep);font-family:'Oswald',sans-serif;font-size:22px;line-height:30px}
.quote{position:absolute;left:556px;top:124px}
.line-arrow{position:absolute;top:279px}

/* footer */
.site-footer{top:2788px;height:302px;background:var(--footer);color:var(--white)}
.site-footer .brand{left:141px;top:74px;color:var(--white)}
.site-footer .brand .mark{background:var(--white)}
.socials{position:absolute;left:215px;top:146px;display:flex;gap:11px}
.socials span{width:26px;height:26px;border:1px solid #ddd;border-radius:50%}
.site-footer h5{position:absolute;top:52px;font-size:19px;font-weight:500}
.quick-links{position:absolute;left:547px;top:98px;list-style:none;font-size:13px}
.quick-links li{margin-bottom:13px;height:17px}
.quick-links li:first-child{text-decoration:underline}
.contact-list{position:absolute;left:828px;top:96px;list-style:none}
.contact-list li{display:flex;gap:14px;align-items:center;height:36px;margin-bottom:13px;font-size:13px;line-height:19px}
.contact-list b{font-weight:600}
.copyright{position:absolute;left:0;top:254px;width:1200px;height:48px;background:var(--blue-deep);text-align:center;line-height:48px;font-size:12px}
</style>
</head>
<body>

<header class="site-header">
  <div class="band-top"></div>
  <div class="band-bottom-right"></div>
  <div class="brand"><span class="mark"></span>Ferravolt</div>
  <nav class="nav">
    <a class="active" href="#">Home</a><a href="#">Skills</a><a href="#">Presentation</a><a href="#">Contact</a>
  </nav>
</header>

<section class="hero" role="img" aria-label="Raffinerie industrielle illuminée au crépuscule">
  <p class="hero-text">Lorem ipsum dolor sit amet, consetetur sadipscing elitr, sed diam nonumy eirmod tempor invidunt ut labore et dolore magna aliquyam erat, sed diam voluptua. At vero eos et accusam et justo duo dolores et ea rebum. Stet clita kasd gubergren, no sea takimata sanctus est Lorem.</p>
  <a class="btn" href="#">Savoir Plus</a>
</section>

<section class="features">
  <div class="feature" style="left:134px">
    <svg width="80" height="72" viewBox="0 0 80 72"><polygon points="0,66 50,10 50,66" fill="#cfcfcf"/><g fill="none" stroke="#1c45a0" stroke-width="2"><rect x="22" y="30" width="26" height="20"/><path d="M48 36h10l7 8v6H48"/><circle cx="30" cy="53" r="4"/><circle cx="58" cy="53" r="4"/><path d="M8 36h10M12 42h8"/></g></svg>
    <h3 class="head-font">Passion<br>for delivery</h3>
    <p>Lorem ipsum dolor sit amet, consectetur adipiscing elit. Phasellus commodo.</p>
  </div>
  <div class="feature" style="left:466px">
    <svg width="80" height="72" viewBox="0 0 80 72"><polygon points="0,66 50,10 50,66" fill="#cfcfcf"/><g fill="none" stroke="#1c45a0" stroke-width="2"><rect x="20" y="28" width="44" height="28" rx="3"/><path d="M20 40h44M32 28v28M52 28v28"/></g></svg>
    <h3 class="head-font">Passion<br>for people</h3>
    <p>Lorem ipsum dolor sit amet, consectetur adipiscing elit. Phasellus commodo.</p>
  </div>
  <div class="feature" style="left:798px">
    <svg width="80" height="72" viewBox="0 0 80 72"><polygon points="0,66 50,10 50,66" fill="#cfcfcf"/><g fill="none" stroke="#1c45a0" stroke-width="2"><circle cx="52" cy="42" r="18"/><path d="M34 42h36M52 24c-8 10-8 26 0 36M52 24c8 10 8 26 0 36"/></g></svg>
    <h3 class="head-font">Passion<br>for environment</h3>
    <p>Lorem ipsum dolor sit amet, consectetur adipiscing elit. Phasellus commodo.</p>
  </div>
</section>

<section class="about">
  <div class="photo" role="img" aria-label="Installation de tuyauterie industrielle en acier"></div>
  <div class="copy">
    <div class="kicker head-font">À propos de</div>
    <h2 class="head-font">Ferravolt</h2>
    <p>Lorem ipsum dolor sit amet, consectetur adipiscing elit. Fusce efficitur libero non ante luctus tincidunt. Curabitur commodo tortor purus, sit amet pellentesque odio Curabitur commodo tortor mattis vel. Suspendisse sit amet magna sed dui dapibus tristique.</p>
    <h4 class="head-font">Vision</h4>
    <p>Fusce egestas purus imperdiet, consequat diam ut, consequat nulla. Maecenas non felis pharetra, porta dolor urna.</p>
    <h4 class="head-font">Values</h4>
    <p>Nullam eu sagittis urna, non rutrum tellus. Proin quis mi lectus. Curabitur id nulla non arcu auctor molestie. Nulla ipsum justo.</p>
    <a class="btn" href="#">Contactez-nous</a>
  </div>
</section>

<section class="skills">
  <h2 class="head-font">Nos compétences</h2>
  <div class="skill" style="left:141px">
    <div class="pic" role="img" aria-label="Tuyauterie inox dans une usine" style="background:linear-gradient(135deg,#d9dde2,#8e98a4)"></div>
    <div class="label head-font">Tuyauterie industrielle<svg class="corner" width="32" height="46" viewBox="0 0 32 46"><polygon points="32,0 32,46 0,46" fill="#333"/><path d="M20 32l5 5-5 5" stroke="#fff" stroke-width="2" fill="none"/></svg></div>
  </div>
  <div class="skill" style="left:454px">
    <div class="pic" role="img" aria-label="Atelier de chaudronnerie sombre" style="background:linear-gradient(135deg,#4a4f55,#1f2226)"></div>
    <div class="label head-font">Chaudronnerie<svg class="corner" width="32" height="46" viewBox="0 0 32 46"><polygon points="32,0 32,46 0,46" fill="#333"/><path d="M20 32l5 5-5 5" stroke="#fff" stroke-width="2" fill="none"/></svg></div>
  </div>
  <div class="skill" style="left:767px">
    <div class="pic" role="img" aria-label="Hall de charpente métallique éclairé" style="background:linear-gradient(135deg,#2e2a26,#8a6a44 60%,#3a342e)"></div>
    <div class="label head-font">Charpente métallique<svg class="corner" width="32" height="46" viewBox="0 0 32 46"><polygon points="32,0 32,46 0,46" fill="#333"/><path d="M20 32l5 5-5 5" stroke="#fff" stroke-width="2" fill="none"/></svg></div>
  </div>
  <a class="btn" href="#">Contactez-nous</a>
</section>

<section class="clients">
  <h2 class="head-font">Nos clients</h2>
  <p class="lead">Aliquam in dignissim leo. Fusce tempus, metus nec hendr rit vehicula, lacus sapien ornare arcu.</p>
  <svg class="round-arrow" style="left:77px" width="44" height="44" viewBox="0 0 44 44"><circle cx="22" cy="22" r="20" fill="#fff" stroke="#1c45a0" stroke-width="1.5"/><path d="M30 22H14M20 16l-6 6 6 6" stroke="#1c45a0" stroke-width="2" fill="none"/></svg>
  <div class="logo-box" style="left:141px"><span class="dot"></span>Norvik</div>
  <div class="logo-box" style="left:327px;font-size:22px"><span class="dot"></span>Caldenhub</div>
  <div class="logo-box" style="left:514px"><span class="dot"></span>Ostra.</div>
  <div class="logo-box" style="left:700px"><span class="dot"></span>Belmo</div>
  <div class="logo-box" style="left:886px"><span class="dot"></span>Quira.</div>
  <svg class="round-arrow" style="left:1079px" width="44" height="44" viewBox="0 0 44 44"><circle cx="22" cy="22" r="20" fill="#fff" stroke="#1c45a0" stroke-width="1.5"/><path d="M14 22h16M24 16l6 6-6 6" stroke="#1c45a0" stroke-width="2" fill="none"/></svg>
</section>

<section class="reviews">
  <h2 class="head-font">Avis clients satisfaits</h2>
  <div class="review-card">
    <p>Lorem ipsum dolor sit amet, consectetuer adipiscing elit, sed diam nonummy nibh euismod tincidunt ut laoreet dolore magna aliquam erat volutpat. Ut wisi enim ad minim veniam, quis nostrud exerci tation ullamcorper suscipit lobortis nisl ut aliquip ex ea commodo consequat. Duis autem vel eum iriure dolor in hendrerit in vulputate velit esse molestie consequat, vel illum dolore eu feugiat nulla facilisis.</p>
    <div class="author">- Lena Moreau</div>
  </div>
  <svg class="quote" width="88" height="66" viewBox="0 0 88 66"><g fill="#1c45a0"><circle cx="20" cy="44" r="20"/><path d="M2 42C2 20 14 6 34 2l2 7C22 14 16 24 16 40z"/><circle cx="66" cy="44" r="20"/><path d="M48 42C48 20 60 6 80 2l2 7C68 14 62 24 62 40z"/></g></svg>
  <svg class="line-arrow" style="left:158px" width="70" height="18" viewBox="0 0 70 18"><path d="M68 9H2M10 2L2 9l8 7" stroke="#888" stroke-width="2" fill="none"/></svg>
  <svg class="line-arrow" style="left:972px" width="70" height="18" viewBox="0 0 70 18"><path d="M2 9h66M60 2l8 7-8 7" stroke="#1c45a0" stroke-width="2" fill="none"/></svg>
</section>

<footer class="site-footer">
  <div class="brand"><span class="mark"></span>Ferravolt</div>
  <div class="socials"><span></span><span></span><span></span></div>
  <h5 style="left:549px">Liens Rapides</h5>
  <ul class="quick-links">
    <li>Maison</li><li>Compétences</li><li>Présentation</li><li>Contactez-nous</li>
  </ul>
  <h5 style="left:830px">Détails Du Contact</h5>
  <ul class="contact-list">
    <li><svg width="36" height="36" viewBox="0 0 36 36"><circle cx="18" cy="18" r="17" fill="none" stroke="#ddd"/><path d="M18 10a6 6 0 0 1 6 6c0 5-6 10-6 10s-6-5-6-10a6 6 0 0 1 6-6z" fill="none" stroke="#fff" stroke-width="1.4"/><circle cx="18" cy="16" r="2" fill="#fff"/></svg><span>45, rue de l'Atelier,<br>Ville, Région 1020</span></li>
    <li><svg width="36" height="36" viewBox="0 0 36 36"><circle cx="18" cy="18" r="17" fill="none" stroke="#ddd"/><path d="M12 11l4 0 1 5-2 2a10 10 0 0 0 5 5l2-2 5 1v4c-9 1-16-6-15-15z" fill="none" stroke="#fff" stroke-width="1.4"/></svg><span><b>Téléphone</b><br>+41-555-0142</span></li>
    <li><svg width="36" height="36" viewBox="0 0 36 36"><circle cx="18" cy="18" r="17" fill="none" stroke="#ddd"/><rect x="10" y="12" width="16" height="12" fill="none" stroke="#fff" stroke-width="1.4"/><path d="M10 12l8 7 8-7" fill="none" stroke="#fff" stroke-width="1.4"/></svg><span><b>E-mail</b><br>info@ferravolt.com</span></li>
  </ul>
  <div class="copyright">© 2023 Ferravolt SA.&nbsp; Tous Droits Réservés</div>
</footer>

</body>
</html>
```